Web Design Project - Shipping Industry

Goals and Objectives
The objective of the new website is to create a more modern look and feel. The site will also allow for a more effective means of communicating with members while providing the public with information and developments in the local, regional and international shipping industry.
Scope
The website will highlight the history of the organisation inclusive of text and photographs. It will take visitors through the years from beginning to present. Information on the history of the shipping industry will also be included.
It will feature current articles on the organisation, its members and stakeholders in the shipping industry. Member information as well as pertinent details regarding the organisation’s subsidiaries will be documented for the website.
Information as it relates to shipping statistics, case studies, laws and regulations, international treaties and trade documents, shipping terms, careers in shipping, job opportunities, training opportunities, information for shippers including port listing and trade lanes will be main features of the content for the website.
The Association’s community involvement, industry calendar events and related links relevant industry members will also be featured.
Target Market
• The General Public;
• Members of the organization;
• Shipping Industry Stakeholders (local, regional and international);
• Tertiary students conducting research.
• Potential employees
• Potential Business Partners
Best Practice Bench Marketing
The following websites are being looked at:
• Korvel Quays - http://www.korvelquays.example/ (preferred look)
• Tidewell Shipping Association - http://www.twa-ships.example/ (like image transition on main page)
• Brolund - http://www.brolund.example (professional look)
• KHW - http://www.kelharbours.example (preferred color: blue in logo)
• Vendlo - http://www.vendlo.example/electronics/tv-video-audio/ (preferred look for links page: image + short text below + visit site link)
Expected Result
• 3 - 5 pages which must include: [1] main page [2] standard page [3] links page
Target Market(s)
The General Public; Members of the organization; Shipping Industry Stakeholders (local, regional and international); Tertiary students conductin
Industry/Entity Type
Shipping

```html
<!DOCTYPE html>
<html lang="en">
<head>
<meta charset="utf-8">
<title>Quayside Data Services</title>
<link rel="stylesheet" href="https://fonts.googleapis.com/css2?family=Source+Sans+3:ital,wght@0,400;0,600;0,700;1,400&display=swap">
<style>
:root{
  --page:#ececec;
  --white:#ffffff;
  --navy:#2b2a6e;
  --ink:#333333;
  --muted:#8a8a8a;
  --blue:#1d6ea6;
  --blue-dark:#175d8e;
  --orange:#f26b1d;
  --green:#3fa63a;
  --rule:#dddddd;
  --placeholder:#e4e4e4;
}
*{box-sizing:border-box;margin:0;padding:0}
html,body{width:1200px;height:997px;overflow:hidden}
body{background:var(--page);font-family:"Source Sans 3",Arial,sans-serif;color:var(--ink)}
.page{position:relative;width:997px;height:997px;margin-left:100px;background:var(--white)}
.abs{position:absolute}
.brand{left:41px;top:46px;font-size:30px;font-weight:600;letter-spacing:5px;color:var(--navy)}
.social{left:657px;top:52px;display:flex;gap:6px}
.social span{width:15px;height:15px;background:var(--blue);border-radius:2px}
.social span:last-child{background:#c9342b}
.search{left:741px;top:47px;width:222px;height:26px;border:1px solid #d0d0d0;font-size:13px;padding:4px 10px;color:#333;display:flex;justify-content:space-between;align-items:center}
.nav{left:39px;top:126px;width:922px;height:43px;border-top:3px solid var(--orange);background:linear-gradient(#fff,#f3f3f3);display:flex;justify-content:space-around;align-items:center;font-size:12.5px}
.nav a{color:#222;text-decoration:none;padding:2px 9px}
.nav a.active{background:var(--orange);color:#fff;border-radius:2px}
.hero{left:39px;top:169px;width:922px;height:314px;background:linear-gradient(90deg,#6f7c86 0%,#b07a55 30%,#8b96a0 50%,#c8603a 75%,#9aa3a9 100%)}
.dropdown{left:132px;top:169px;width:167px;background:#f4f4f4}
.dropdown li{list-style:none;height:31px;line-height:31px;padding-left:15px;font-size:12px;border-bottom:1px solid #dcdcdc}
.band{left:39px;top:483px;width:922px;height:73px;background:linear-gradient(var(--blue),var(--blue-dark));color:#fff}
.band h1{position:absolute;left:24px;top:16px;font-size:33px;font-weight:600}
.band p{position:absolute;left:424px;top:14px;width:465px;font-size:14.5px;line-height:21px}
.band b{font-weight:600;margin-left:6px}
.arrow{display:inline-block;width:13px;height:13px;vertical-align:-2px;margin-left:4px}
.intro-mark{left:57px;top:592px;width:62px;height:62px;background:var(--placeholder)}
.intro{left:146px;top:597px;width:495px;font-size:13.5px;line-height:20.5px;letter-spacing:-0.2px}
.intro strong{font-weight:600}
.card{top:702px;width:183px}
.card h3{height:28px;line-height:28px;padding-left:11px;color:#fff;font-weight:400;font-size:13px}
.card .photo{height:101px}
.card p{font-size:10.5px;line-height:15px;margin-top:8px}
.card .more{margin-top:10px;font-size:11.5px;font-weight:700}
.news{left:681px;top:584px;width:283px}
.news h2{font-size:21px;font-weight:400;margin-bottom:9px}
.news h4{font-size:13.5px;font-weight:700;line-height:18.5px;width:250px}
.news time{display:block;color:var(--muted);font-style:italic;font-size:13px;margin:2px 0 5px}
.news p{font-size:12.4px;line-height:18.5px}
.news a{color:var(--orange);text-decoration:none}
.news article+article{margin-top:27px}
.footer{left:0;top:952px;width:997px;border-top:1px solid var(--rule);font-size:10.5px;color:var(--muted)}
.footer .copy{position:absolute;left:39px;top:18px}
.footer .links{position:absolute;right:55px;top:18px;word-spacing:2px}
</style>
</head>
<body>
<div class="page">
  <div class="abs brand">HARBORLINE</div>
  <div class="abs social"><span></span><span></span><span></span><span></span></div>
  <div class="abs search">Search
    <svg width="14" height="14" viewBox="0 0 14 14"><circle cx="8" cy="6" r="4.5" fill="none" stroke="#aaa" stroke-width="1.4"/><line x1="5" y1="9" x2="1" y2="13" stroke="#aaa" stroke-width="1.6"/></svg>
  </div>

  <nav class="abs nav">
    <a>HOME</a><a class="active">ABOUT US</a><a>PRODUCTS</a><a>SERVICES</a><a>NEWS</a><a>SUPPORT</a><a>PARTNERS</a><a>CUSTOMERS</a><a>CONTACT</a>
  </nav>

  <div class="abs hero" role="img" aria-label="Port workers in hard hats and safety vests beside stacked shipping containers and cranes"></div>
  <ul class="abs dropdown">
    <li>Milestones</li><li>Vision</li><li>Board of Directors</li><li>Management Team</li>
  </ul>

  <div class="abs band">
    <h1>Quayside Data Services</h1>
    <p>Built for operation in a port or agent environment, it is a powerful platform to manage their operations and drive efficiencies <b>LEARN MORE</b>
      <svg class="arrow" viewBox="0 0 14 14"><circle cx="7" cy="7" r="7" fill="#fff"/><path d="M4 7h6M7.5 4.5L10 7l-2.5 2.5" fill="none" stroke="var(--blue)" stroke-width="1.6"/></svg></p>
  </div>

  <div class="abs intro-mark" role="img" aria-label="Company emblem"></div>
  <p class="abs intro"><strong>Quayside Data Services</strong> (HARBORLINE), a subsidiary of the Marlow Shipping Association, was established in 1981 to provide information technology infrastructure and systems support to the local port community and the wider Caribbean maritime sector.</p>

  <div class="abs card" style="left:41px">
    <h3 style="background:var(--blue)">CAREERS IN SHIPPING</h3>
    <div class="photo" role="img" aria-label="Dock workers in safety vests walking along a container quay" style="background:linear-gradient(#7d95b0,#b8894f)"></div>
    <p>Lorem ipsum dolor sit amet, consectetur adipisicing elit, sed do eiusmod tempor incididunt ut labore et dolore magna</p>
    <div class="more" style="color:var(--blue)">LEARN MORE <svg class="arrow" viewBox="0 0 14 14"><circle cx="7" cy="7" r="7" fill="var(--blue)"/><path d="M4 7h6M7.5 4.5L10 7l-2.5 2.5" fill="none" stroke="#fff" stroke-width="1.6"/></svg></div>
  </div>
  <div class="abs card" style="left:248px">
    <h3 style="background:var(--green)">JOB OPPORTUNITIES</h3>
    <div class="photo" role="img" aria-label="Operators working at computer monitors in a control room" style="background:linear-gradient(#3c6f6a,#9fb1ad)"></div>
    <p>Lorem ipsum dolor sit amet, consectetur adipisicing elit, sed do eiusmod tempor incididunt ut labore et dolore magna</p>
    <div class="more" style="color:var(--green)">LEARN MORE <svg class="arrow" viewBox="0 0 14 14"><circle cx="7" cy="7" r="7" fill="var(--green)"/><path d="M4 7h6M7.5 4.5L10 7l-2.5 2.5" fill="none" stroke="#fff" stroke-width="1.6"/></svg></div>
  </div>
  <div class="abs card" style="left:458px">
    <h3 style="background:var(--orange)">TRAINING OPPORTUNITIES</h3>
    <div class="photo" role="img" aria-label="Two workers reviewing plans on a laptop in a warehouse" style="background:linear-gradient(#b99a72,#6d6a5c)"></div>
    <p>Lorem ipsum dolor sit amet, consectetur adipisicing elit, sed do eiusmod tempor incididunt ut labore et dolore magna</p>
    <div class="more" style="color:var(--orange)">LEARN MORE <svg class="arrow" viewBox="0 0 14 14"><circle cx="7" cy="7" r="7" fill="var(--orange)"/><path d="M4 7h6M7.5 4.5L10 7l-2.5 2.5" fill="none" stroke="#fff" stroke-width="1.6"/></svg></div>
  </div>

  <section class="abs news">
    <h2>LATEST NEWS</h2>
    <article>
      <h4>QDS Launches Document Management Software</h4>
      <time>March 10, 2012</time>
      <p>Quayside Data Services Limited (QDS), along with its partner Eastmere Systems Incorporated, presented the Ledgerly Enterprise Document Management Software during a seminar held at the Halcyon Hotel last Wednesday. <a>Read more »</a></p>
    </article>
    <article>
      <h4>Business Continuity - Are you prepared ?</h4>
      <time>March 8, 2012</time>
      <p>Business continuity should be the number one priority of every organization, since failure to have a contingency plan has repeatedly proven to be catastrophic for organizations. <a>Read more »</a></p>
    </article>
  </section>

  <footer class="abs footer">
    <span class="copy">© QUAYSIDE DATA SERVICES | ALL RIGHT RESERVED</span>
    <span class="links">LEGAL NOTICE &nbsp; | &nbsp; PRIVACY POLICY &nbsp; | &nbsp; CONTACT US</span>
  </footer>
</div>
</body>
</html>
```